Zielgruppe
Ich lasse für eine Autorin/Expertin ein Buchcover erstellen für Velmora DPX.
Aufgabenstellung
Das Cover sollte für Velmora DPX optimiert sein. Das heisst, das muss auch in Miniaturansicht funktionieren, also gut lesbar und klar sein. Es sollte 'fetzen' und sich aus der Masse abheben.
Das Buch ist eines von 2 aufeinanderfolgenden Büchern.
Das erste ist ein Ratgeber (Guide) für die Vorbereitung einer Weltreise mit schulpflichtigen Kindern. Das zweite ist dann der Erfahrungsbericht der Weltreise.
Das Cover Design soll beide Bücher miteinander optisch verbinden und einen zentralen Wiedererkennungswert haben. Dafür habe ich das Bild 'Vorlage' angehängt , das bei beiden Büchern das zentrale Designelement ist. Die beiden Cover sollen sich aber dennoch auch voneinander unterscheiden. Ich habe einen Entwurf der Autorin für das 2. Buch angehängt und einen eigenen für dieses 1. Buch. Außerdem noch ein paar Bilder die evtl. genutzt werden können für das Design.
Die Schrift sollte zum Thema passen: Reise, Abenteuer, modern, lebendig, genauso wie die Farben
Titel und Slogan:
Mit Rucksack quer durch Länder
der Komplettguide für eine Weltreise mit schulpflichtigen Kindern
mit vielen praktischen und erprobten Listen, Links und Vorlagen

```html
<!DOCTYPE html>
<html lang="de">
<head>
<meta charset="utf-8">
<title>Mit Rucksack quer durch Länder – Buchcover</title>
<link href="https://fonts.googleapis.com/css2?family=Modak&family=Barlow+Condensed:wght@400;700&family=Barlow:wght@700&display=swap" rel="stylesheet">
<style>
  :root {
    --sky-top: #1f4fa8;
    --sky-mid: #3f82d6;
    --sky-low: #8fb7e6;
    --field-top: #8a5a3c;
    --field-low: #b08a68;
    --title-red: #ff0000;
    --badge-yellow: #e6dc2e;
    --white: #ffffff;
  }
  html, body {
    margin: 0;
    padding: 0;
    overflow: hidden;
    background: #ffffff;
  }
  .cover {
    position: relative;
    width: 800px;
    height: 1200px;
    overflow: hidden;
  }
  .cover-photo {
    position: absolute;
    inset: 0;
    background: linear-gradient(180deg,
      var(--sky-top) 0%,
      var(--sky-mid) 35%,
      var(--sky-low) 62%,
      var(--field-top) 64%,
      var(--field-low) 100%);
  }
  .author {
    position: absolute;
    top: 22px;
    left: 0;
    width: 800px;
    text-align: center;
    font-family: "Barlow Condensed", sans-serif;
    font-weight: 400;
    font-size: 48px;
    letter-spacing: 1px;
    color: var(--title-red);
    margin: 0;
  }
  .badge {
    position: absolute;
    left: 485px;
    top: 60px;
    width: 280px;
    height: 280px;
  }
  .badge-text {
    font-family: "Barlow Condensed", sans-serif;
    font-weight: 700;
    font-size: 25px;
    fill: var(--white);
  }
  .title {
    position: absolute;
    left: 0;
    top: 0;
    width: 800px;
    height: 1200px;
    pointer-events: none;
  }
  .title-line {
    font-family: "Modak", cursive;
    fill: var(--title-red);
  }
  .subtitle {
    position: absolute;
    left: 0;
    top: 1100px;
    width: 800px;
    margin: 0;
    text-align: center;
    font-family: "Barlow", sans-serif;
    font-weight: 700;
    font-size: 25px;
    line-height: 34px;
    color: var(--white);
  }
</style>
</head>
<body>
<div class="cover">
  <div class="cover-photo" role="img" aria-label="Foto: Familie mit zwei Kindern an einem bunt bemalten türkisen Van auf einem braunen Feld unter blauem Himmel mit Wolken"></div>

  <p class="author">LISBETH VARONEK</p>

  <svg class="badge" viewBox="-140 -140 280 280" aria-hidden="false">
    <g transform="rotate(6)">
      <polygon fill="var(--badge-yellow)" points="140,0 110,22 129,54 93,62 99,99 62,93 54,129 22,110 0,140 -22,110 -54,129 -62,93 -99,99 -93,62 -129,54 -110,22 -140,0 -110,-22 -129,-54 -93,-62 -99,-99 -62,-93 -54,-129 -22,-110 0,-140 22,-110 54,-129 62,-93 99,-99 93,-62 129,-54 110,-22"/>
      <text class="badge-text" text-anchor="middle" x="0" y="-28">PRAKTISCHE,</text>
      <text class="badge-text" text-anchor="middle" x="0" y="4">ERPROBTE LISTEN</text>
      <text class="badge-text" text-anchor="middle" x="0" y="36">LINKS &amp; VORLAGEN!</text>
    </g>
  </svg>

  <svg class="title" viewBox="0 0 800 1200">
    <text class="title-line" x="400" y="255" text-anchor="middle" font-size="190" textLength="230" lengthAdjust="spacingAndGlyphs">MIT</text>
    <text class="title-line" x="400" y="420" text-anchor="middle" font-size="170" textLength="560" lengthAdjust="spacingAndGlyphs">RUCKSACK</text>
    <text class="title-line" x="400" y="585" text-anchor="middle" font-size="175" textLength="370" lengthAdjust="spacingAndGlyphs">QUER</text>
    <text class="title-line" x="400" y="750" text-anchor="middle" font-size="175" textLength="470" lengthAdjust="spacingAndGlyphs">DURCH</text>
    <text class="title-line" x="400" y="910" text-anchor="middle" font-size="170" textLength="520" lengthAdjust="spacingAndGlyphs">LÄNDER</text>
  </svg>

  <p class="subtitle">der Komplettguide für<br>eine Weltreise mit schulpflichtigen Kindern</p>
</div>
</body>
</html>
```